Office Template for Whitepapers

We are looking for a whitepaper design template. We will be publishing a series of whitepapers with an ISBN on our website and in print. The target audiences are top executives in the capital intensive industry and government officials. Our aim is to publish a book later on, once we have collected enough whitepapers. If we are satisfied with the design, the winning designer will also be hired to design the book format and cover.
Requirements:
-The whitepapers will be published both online and in print so hard-to-read fonts or black backgrounds are not an option.
-The template is prepared in an MS Office program, preferably Word or PowerPoint. The template allows for different lengths of text, inclusion of graphs and other images, as well as some customization regarding the cover page (title, main image).
-The template should include at least:
o Cover page
o Summary page
o Main text design (header / footer / section titles on different levels )
o A page with information about the authors and thank-you notes to contributors
o Back cover page including our logo and contact details and ISBN number.
- Within the main text a few exhibits (graphs) and text boxes will be included, so we also need a template for graphs and text boxes.
- The whitepaper should be more or less consistent with our website design. Fonts used are Futura Std Book, Futura Std Medium, Arial, and Adobe Garamond Pro. The main colors are dark blue and purple (see our website).
- We are looking for A5 size, portrait. The whitepapers will each be 20 to 50 pages long.
Attached with this brief are:
-The company logo
-Some images that may be used for designing the template (but you are also welcome to use your own images)
-An example of a whitepaper (we are looking for a similar format, but different layout)
-A previously published brochure
Website: www.brovantiq.nl
Corporate colors: RGB: 129.64.156, 19.0.124. Hexa: #81409C, #13007C
Reason: I've extended the deadline, because I am still very curious about the additional designs from Rosalind and Velvet Lantern. Both of them have submitted promising cover design and we would like to see their ideas for the inside of the whitepaper.

```html
<!DOCTYPE html>
<html lang="en">
<head>
<meta charset="utf-8">
<title>Whitepaper Cover – Brovantiq</title>
<link rel="stylesheet" href="https://fonts.googleapis.com/css2?family=Jost:wght@400;500&display=swap">
<style>
  :root {
    --paper: #ffffff;
    --navy: #13007c;
    --purple: #81409c;
    --title-blue: #2d5f8e;
    --sub-blue: #3a6a9a;
    --tile-gap: #0a1e5e;
    --tile-deep: #0e2f86;
    --tile-mid: #1f5fc0;
    --tile-bright: #2f86d8;
    --tile-light: #5ab8ec;
    --tile-ink: #12205a;
    --frame-teal: #3a9fb6;
  }
  * { margin: 0; padding: 0; box-sizing: border-box; }
  html, body {
    width: 843px;
    height: 1200px;
    overflow: hidden;
    background: var(--paper);
  }
  .cover {
    position: relative;
    width: 843px;
    height: 1200px;
    background: var(--paper);
    font-family: "Jost", "Futura", sans-serif;
    overflow: hidden;
  }

  /* Photo mosaic bands */
  .mosaic {
    position: absolute;
    left: 0;
    width: 843px;
    display: grid;
    grid-template-columns: repeat(9, 1fr);
    gap: 2px;
    background: var(--tile-gap);
  }
  .mosaic--top { top: 0; height: 337px; grid-template-rows: repeat(5, 1fr); }
  .mosaic--bottom { top: 880px; height: 320px; grid-template-rows: repeat(5, 1fr); }
  .mosaic__tile { background: linear-gradient(135deg, var(--tile-mid), var(--tile-deep)); }
  .mosaic__tile:nth-child(4n+1) { background: linear-gradient(160deg, var(--tile-light) 0%, var(--tile-mid) 70%); }
  .mosaic__tile:nth-child(5n+2) { background: linear-gradient(200deg, var(--tile-bright) 0%, var(--tile-ink) 100%); }
  .mosaic__tile:nth-child(7n+3) { background: radial-gradient(circle at 60% 40%, var(--tile-light) 0%, var(--tile-deep) 80%); }
  .mosaic__tile:nth-child(6n+4) { background: linear-gradient(90deg, var(--tile-deep) 0%, var(--tile-bright) 100%); }
  .mosaic__tile:nth-child(9n+6) { background: linear-gradient(180deg, var(--tile-ink) 0%, var(--tile-mid) 100%); }
  .mosaic__tile:nth-child(8n+7) { background: radial-gradient(circle at 40% 60%, var(--tile-bright) 0%, var(--tile-ink) 90%); }

  /* Brand */
  .brand {
    position: absolute;
    left: 40px;
    top: 393px;
    display: flex;
    align-items: center;
    gap: 10px;
  }
  .brand__mark {
    width: 64px;
    height: 64px;
    background: var(--navy);
  }
  .brand__text { display: flex; flex-direction: column; }
  .brand__name {
    font-weight: 500;
    font-size: 46px;
    line-height: 1;
    letter-spacing: 11px;
    color: var(--navy);
    text-transform: uppercase;
  }
  .brand__tagline {
    margin-top: 5px;
    font-weight: 400;
    font-size: 19px;
    line-height: 1;
    letter-spacing: 11.5px;
    color: var(--purple);
    text-transform: uppercase;
  }

  /* Titles */
  .cover-title {
    position: absolute;
    left: 156px;
    top: 530px;
    font-weight: 400;
    font-size: 60px;
    line-height: 1.2;
    color: var(--title-blue);
    white-space: nowrap;
  }
  .cover-subtitle {
    position: absolute;
    left: 316px;
    top: 616px;
    font-weight: 400;
    font-size: 37px;
    line-height: 1.2;
    color: var(--sub-blue);
    white-space: nowrap;
  }

  /* Image placeholders */
  .image-frames {
    position: absolute;
    left: 0;
    top: 0;
    width: 843px;
    height: 1200px;
  }
  .image-frame {
    fill: var(--paper);
    stroke: var(--frame-teal);
    stroke-width: 2.2;
    stroke-dasharray: 8 5;
  }
</style>
</head>
<body>
  <main class="cover">
    <div class="mosaic mosaic--top" role="img" aria-label="Mosaic of blue-toned photo tiles: light bulbs, wind turbines, waveforms, chess pieces, keyboards and circuitry">
      <span class="mosaic__tile"></span><span class="mosaic__tile"></span><span class="mosaic__tile"></span><span class="mosaic__tile"></span><span class="mosaic__tile"></span><span class="mosaic__tile"></span><span class="mosaic__tile"></span><span class="mosaic__tile"></span><span class="mosaic__tile"></span>
      <span class="mosaic__tile"></span><span class="mosaic__tile"></span><span class="mosaic__tile"></span><span class="mosaic__tile"></span><span class="mosaic__tile"></span><span class="mosaic__tile"></span><span class="mosaic__tile"></span><span class="mosaic__tile"></span><span class="mosaic__tile"></span>
      <span class="mosaic__tile"></span><span class="mosaic__tile"></span><span class="mosaic__tile"></span><span class="mosaic__tile"></span><span class="mosaic__tile"></span><span class="mosaic__tile"></span><span class="mosaic__tile"></span><span class="mosaic__tile"></span><span class="mosaic__tile"></span>
      <span class="mosaic__tile"></span><span class="mosaic__tile"></span><span class="mosaic__tile"></span><span class="mosaic__tile"></span><span class="mosaic__tile"></span><span class="mosaic__tile"></span><span class="mosaic__tile"></span><span class="mosaic__tile"></span><span class="mosaic__tile"></span>
      <span class="mosaic__tile"></span><span class="mosaic__tile"></span><span class="mosaic__tile"></span><span class="mosaic__tile"></span><span class="mosaic__tile"></span><span class="mosaic__tile"></span><span class="mosaic__tile"></span><span class="mosaic__tile"></span><span class="mosaic__tile"></span>
    </div>

    <div class="mosaic mosaic--bottom" role="img" aria-label="Mosaic of blue-toned photo tiles: waveforms, light bulbs, keyboards, chess pieces and wind turbines">
      <span class="mosaic__tile"></span><span class="mosaic__tile"></span><span class="mosaic__tile"></span><span class="mosaic__tile"></span><span class="mosaic__tile"></span><span class="mosaic__tile"></span><span class="mosaic__tile"></span><span class="mosaic__tile"></span><span class="mosaic__tile"></span>
      <span class="mosaic__tile"></span><span class="mosaic__tile"></span><span class="mosaic__tile"></span><span class="mosaic__tile"></span><span class="mosaic__tile"></span><span class="mosaic__tile"></span><span class="mosaic__tile"></span><span class="mosaic__tile"></span><span class="mosaic__tile"></span>
      <span class="mosaic__tile"></span><span class="mosaic__tile"></span><span class="mosaic__tile"></span><span class="mosaic__tile"></span><span class="mosaic__tile"></span><span class="mosaic__tile"></span><span class="mosaic__tile"></span><span class="mosaic__tile"></span><span class="mosaic__tile"></span>
      <span class="mosaic__tile"></span><span class="mosaic__tile"></span><span class="mosaic__tile"></span><span class="mosaic__tile"></span><span class="mosaic__tile"></span><span class="mosaic__tile"></span><span class="mosaic__tile"></span><span class="mosaic__tile"></span><span class="mosaic__tile"></span>
      <span class="mosaic__tile"></span><span class="mosaic__tile"></span><span class="mosaic__tile"></span><span class="mosaic__tile"></span><span class="mosaic__tile"></span><span class="mosaic__tile"></span><span class="mosaic__tile"></span><span class="mosaic__tile"></span><span class="mosaic__tile"></span>
    </div>

    <div class="brand">
      <div class="brand__mark"></div>
      <div class="brand__text">
        <span class="brand__name">Brovantiq</span>
        <span class="brand__tagline">Decision Support</span>
      </div>
    </div>

    <h1 class="cover-title">Whitepaper Title Text</h1>
    <p class="cover-subtitle">Subtitle Placeholder Text</p>

    <svg class="image-frames" viewBox="0 0 843 1200" aria-hidden="true">
      <polygon class="image-frame image-frame--main" points="53,828 444,697 542,992 156,1124"/>
      <polygon class="image-frame image-frame--secondary" points="524,737 760,850 642,1053 424,943"/>
    </svg>
  </main>
</body>
</html>
```